brightquokka.net we need a webpage designed for our new product

We need a webpage designed for our new range of products from our new brand. We have had a logo designed on sketchharbor (see attached) and we want to keep to this theme. Our first product is a range of affordable app controlled LED lightbulbs.

I have added some photos that we think is good inspirational material and would be good as a background to this website, but we want the site to look modern but not conventional. We would like something that makes our company look quirky not corporate.

Thats it

Target Market(s)

Our product is being stocked by big name online retailers in the UK, the page will get link through hits from our app. Our target market is gadget freaks of all ages.

Industry/Entity Type

It Company

Requirements
Must have
• We are going to need a help page, text to be uploaded next few days.

We need a contact page.

design my work on iOS and Android as most people will access page through their handset or tablet.
Should not have
• We do not want anything too corporate.

```html
<!DOCTYPE html>
<html lang="en">
<head>
<meta charset="utf-8">
<title>BrightQuokka – Controlled LED Lightbulbs</title>
<link href="https://fonts.googleapis.com/css2?family=Open+Sans:ital,wght@0,400;0,600;1,400&display=swap" rel="stylesheet">
<style>
  :root {
    --green: #2e9a2e;
    --green-light: #4db84a;
    --green-dark: #17751b;
    --green-deep: #0f5e14;
    --orange: #f08a0c;
    --orange-light: #f9a01b;
    --text: #222;
    --text-soft: #707070;
    --rule: #dcdcdc;
    --footer-bg: #f4f4f4;
    --white: #fff;
  }
  * { box-sizing: border-box; margin: 0; padding: 0; }
  html, body { width: 1200px; height: 1166px; overflow: hidden; }
  body { font-family: "Open Sans", Arial, sans-serif; color: var(--text); background: var(--white); position: relative; }

  .backdrop {
    position: absolute; inset: 0 0 auto 0; height: 880px;
    background:
      linear-gradient(to bottom, rgba(255,255,255,0) 0, rgba(255,255,255,0) 620px, #fff 860px),
      linear-gradient(90deg, #5a3a22 0%, #8a5a36 8%, #6b7c80 14%, #b08a60 30%, #8c6a48 70%, #a07a58 86%, #c9a27c 100%);
  }

  .page { position: absolute; left: 149px; top: 85px; width: 904px; height: 973px; background: var(--white); }

  .logo-box {
    position: absolute; left: 149px; top: 0; width: 173px; height: 196px;
    background: var(--white); border-radius: 0 0 10px 10px;
    display: flex; align-items: flex-end; justify-content: center; padding-bottom: 16px;
  }
  .logo-name { font-size: 10px; font-weight: 600; letter-spacing: .3px; color: var(--green); text-transform: uppercase; }

  .main-nav { position: absolute; left: 322px; top: 93px; width: 722px; height: 53px; display: flex;
    background: linear-gradient(to bottom, var(--green) 0%, var(--green-dark) 100%); }
  .main-nav a { display: flex; align-items: center; justify-content: center; color: var(--white);
    font-size: 14.5px; text-decoration: none; border-right: 1px solid rgba(0,0,0,.18); }
  .main-nav a:last-child { border-right: 0; }
  .main-nav a.active { background: var(--green-deep); }

  .hero { position: absolute; left: 158px; top: 146px; width: 886px; height: 375px; overflow: hidden;
    background: linear-gradient(to bottom, var(--green-light) 0%, var(--green) 55%, var(--green-dark) 100%); }
  .hero-art { position: absolute; left: 514px; top: 46px; width: 300px; height: 329px;
    background: radial-gradient(circle at 55% 40%, #d8f06a 0%, #8fd34a 25%, rgba(70,170,60,0) 65%); }
  .hero-kicker { position: absolute; left: 58px; top: 108px; font-size: 22px; color: var(--white); }
  .hero-title { position: absolute; left: 58px; top: 137px; font-size: 34px; color: var(--white); font-weight: 400; }
  .hero-text { position: absolute; left: 59px; top: 183px; width: 400px; font-size: 11.5px; line-height: 19px; color: rgba(255,255,255,.6); }
  .hero-dots { position: absolute; left: 61px; top: 235px; display: flex; gap: 3px; }
  .hero-dots span { width: 12px; height: 12px; border-radius: 50%; background: #155c17; }
  .hero-dots span.on { background: var(--white); }

  .features { position: absolute; left: 158px; top: 521px; width: 886px; height: 181px; display: flex;
    border-bottom: 1px solid var(--rule); background: linear-gradient(to bottom, #fff 40%, #f6f6f6 100%); }
  .feature { position: relative; flex: 1; border-right: 1px solid var(--rule); }
  .feature:last-child { border-right: 0; }
  .feature svg { position: absolute; left: 22px; top: 38px; }
  .feature h3 { position: absolute; left: 86px; top: 36px; font-size: 18px; font-weight: 400; color: var(--orange); }
  .feature p { position: absolute; left: 87px; top: 62px; width: 210px; font-size: 11.5px; line-height: 17.5px; color: var(--text-soft); }
  .btn { display: inline-flex; align-items: center; justify-content: center; color: var(--white); font-size: 10.5px; text-decoration: none; border-radius: 3px; }
  .btn-orange { position: absolute; left: 87px; top: 121px; width: 90px; height: 26px;
    background: linear-gradient(to bottom, var(--orange-light), var(--orange)); }
  .btn-green { position: absolute; width: 101px; height: 30px; top: 964px;
    background: linear-gradient(to bottom, var(--green), var(--green-deep)); }

  .section-title { position: absolute; top: 734px; font-size: 26px; font-weight: 400; color: var(--text); }
  .section-title.green { color: var(--green-dark); }
  .copy { position: absolute; font-size: 11.5px; line-height: 19.2px; color: var(--text-soft); }
  .app-photo { position: absolute; left: 495px; top: 776px; width: 251px; height: 115px;
    background: radial-gradient(circle at 50% 40%, #f6d58a 0%, #c08a4a 45%, #5a3a22 100%); }
  .quote { font-style: italic; }
  .author { position: absolute; font-size: 12.5px; color: var(--text); }

  .site-footer { position: absolute; left: 0; top: 1058px; width: 1200px; height: 108px; background: var(--footer-bg); border-top: 1px solid var(--rule); }
  .footer-nav { position: absolute; left: 186px; top: 26px; font-size: 12.5px; color: #444; }
  .footer-nav a { color: #444; text-decoration: none; }
  .footer-nav .sep { margin: 0 7px; }
  .legal { position: absolute; left: 186px; top: 52px; font-size: 12px; color: var(--text-soft); }
  .social { position: absolute; left: 928px; top: 30px; display: flex; gap: 8px; }
  .social span { width: 21px; height: 21px; border-radius: 2px; }
</style>
</head>
<body>
  <div class="backdrop" role="img" aria-label="Photo of a vintage lamp and antiques shop with hanging lights"></div>
  <div class="page"></div>

  <div class="logo-box"><span class="logo-name">BrightQuokka</span></div>

  <nav class="main-nav">
    <a class="active" style="width:89px" href="#">MAIN</a>
    <a style="width:103px" href="#">ABOUT US</a>
    <a style="width:96px" href="#">SERVICES</a>
    <a style="width:116px" href="#">DOWNLOAD</a>
    <a style="width:110px" href="#">SOLUTIONS</a>
    <a style="width:96px" href="#">SUPPORT</a>
    <a style="width:112px" href="#">CONTACT</a>
  </nav>

  <section class="hero">
    <div class="hero-art" role="img" aria-label="Three glowing lightbulbs on cables: spiral, LED and classic bulb"></div>
    <p class="hero-kicker">Aliquam nec erat at purus cursus</p>
    <h1 class="hero-title">Controlled LED Lightbulbs</h1>
    <p class="hero-text">Curabitur metus ipsum luctus eu malesuada ut tincidunt sed diam Donec quis mi sed magna hendrerit accumsan Suspendisse risus</p>
    <div class="hero-dots"><span class="on"></span><span></span><span></span><span></span></div>
  </section>

  <section class="features">
    <div class="feature">
      <svg width="56" height="76" viewBox="0 0 56 76" fill="none" stroke="#2e9a2e" stroke-width="5" stroke-linecap="round">
        <path d="M28 34 C10 30 4 18 6 6 C20 6 28 16 28 34 Z" fill="#2e9a2e" stroke="none"/>
        <path d="M28 34 C46 30 52 18 50 6 C36 6 28 16 28 34 Z" fill="#2e9a2e" stroke="none"/>
        <path d="M14 40 H42 M15 50 H41 M17 60 H39 M22 69 H34"/>
      </svg>
      <h3>WHY CONTROLLED</h3>
      <p>Donec scelerisque leo ac risus Praesent sit amet est In dictum dolor eu dictum porttitor</p>
      <a class="btn btn-orange" href="#">READ MORE</a>
    </div>
    <div class="feature">
      <svg width="56" height="76" viewBox="0 0 56 76"><path d="M40 0 L4 44 H24 L14 74 L52 26 H32 Z" fill="#2e9a2e"/></svg>
      <h3>FEATURE SERVICE</h3>
      <p>Donec scelerisque leo ac risus Praesent sit amet est In dictum dolor eu dictum porttitor</p>
      <a class="btn btn-orange" href="#">READ MORE</a>
    </div>
    <div class="feature">
      <svg width="56" height="76" viewBox="0 0 56 76" fill="none" stroke="#2e9a2e" stroke-width="7" stroke-linecap="round">
        <path d="M18 48 C6 42 4 30 4 26 A24 24 0 0 1 52 26 C52 30 50 42 38 48 Z"/>
        <path d="M20 60 H36 M24 70 H32" stroke-width="5"/>
      </svg>
      <h3>HOW IT WORKS</h3>
      <p>Donec scelerisque leo ac risus Praesent sit amet est In dictum dolor eu dictum porttitor</p>
      <a class="btn btn-orange" href="#">READ MORE</a>
    </div>
  </section>

  <h2 class="section-title" style="left:181px">About Our Company</h2>
  <p class="copy" style="left:181px;top:774px;width:290px">Donec iaculis diam a nisi accumsan viverra Duis sed tellus et tortor vestibulum gravida Praesent elemen-tum elit at tellus Curabitur metus ipsum luctus eu malesuada ut tincidunt</p>
  <p class="copy" style="left:181px;top:855px;width:295px">Donec quis mi sed magna hendrerit accumsan Suspendisse risus nibh ultricies eu volutpat non condi-mentum hendrerit augue Etiam eleifend metus vitae adipiscing semper mauris ipsum iaculis elit congue gravida elit mi egestas orci Curabitur pede</p>
  <a class="btn btn-green" style="left:180px" href="#">READ MORE</a>

  <h2 class="section-title" style="left:495px">Download Our App</h2>
  <div class="app-photo" role="img" aria-label="Photo of a shop interior filled with glowing chandeliers"></div>
  <p class="copy" style="left:496px;top:895px;width:255px">Donec iaculis diam a nisi accumsan viverra Duis sed tellus et tortor vestibulum gravida Praesent elementum elit at tellus Curabitur metus</p>
  <a class="btn btn-green" style="left:498px" href="#">DOWNLOAD</a>

  <h2 class="section-title green" style="left:780px">Testimonials</h2>
  <p class="copy quote" style="left:783px;top:774px;width:250px">Donec iaculis diam a nisi accumsan viverra Duis sed tellus et tortor vestibulum gravida Praesent elementum elit at tellus Curabitur metus ipsum luctus eu malesuada ut tincidunt sed</p>
  <p class="author" style="left:783px;top:852px">By Author Name</p>
  <p class="copy quote" style="left:782px;top:892px;width:250px">Aliquam nec erat at purus cursus interdum Vestibulum ligula augue bibendum accumsan vestibulum ut commodo a mi</p>
  <p class="author" style="left:782px;top:955px">By Author Name</p>

  <footer class="site-footer">
    <nav class="footer-nav">
      <a href="#">MAIN</a><span class="sep">|</span><a href="#">ABOUT US</a><span class="sep">|</span><a href="#">SERVICES</a><span class="sep">|</span><a href="#">DOWNLOAD</a><span class="sep">|</span><a href="#">SOLUTIONS</a><span class="sep">|</span><a href="#">SUPPORT</a><span class="sep">|</span><a href="#">CONTACT</a>
    </nav>
    <p class="legal">© 2014 Company Name&nbsp; All right reserved&nbsp; Term of Use</p>
    <div class="social">
      <span style="background:#3b5998"></span>
      <span style="background:#4fb8e8"></span>
      <span style="background:#1a6fa8"></span>
    </div>
  </footer>
</body>
</html>
```